Corvane Project Services - Flyer

Project Breif:
I need a single page A4 Capability Statement, which will be used to market our services to prospective clients, both in print and via email PDF.
It needs to look professional and should incorporate the elements I have uploaded into files, these include:
Capability Statement Text
Corvane Services Company Logo
Additional Logo’s (Tools We Use)
Glimmer Bay Pics can be cut into the page
I have included examples of capability statements as a guide to what i am looking for.
Regards
Derek
Engineering Consulting

```html
<!DOCTYPE html>
<html lang="en">
<head>
<meta charset="utf-8">
<title>Corvane Project Services – Capability Statement</title>
<link rel="stylesheet" href="https://fonts.googleapis.com/css2?family=Montserrat:wght@500;600;700;800;900&family=Raleway:wght@400;500;600;700&display=swap">
<style>
:root{
  --blue:#5b9bd5;
  --blue-head:#6aa3db;
  --blue-deep:#3a6bb4;
  --blue-panel:#3c6fb6;
  --blue-band:#4c86c6;
  --sky:#8ec4ea;
  --ink:#1b1b1b;
  --text:#2a2a2a;
  --paper:#ffffff;
  --paper-soft:#f3f4f6;
  --white:#ffffff;
}
*{box-sizing:border-box;margin:0;padding:0}
html,body{width:880px;height:1200px;overflow:hidden;background:var(--paper)}
body{font-family:"Raleway",Arial,sans-serif;color:var(--text)}
.flyer{position:relative;width:880px;height:1200px;background:var(--paper);overflow:hidden}
.top-strip{position:absolute;left:0;top:0;width:880px;height:11px;background:var(--sky)}

/* header */
.brand{position:absolute;left:40px;top:30px;width:210px;text-align:center}
.brand-mark{width:52px;height:52px;border-radius:50%;background:var(--blue-deep);margin:0 auto 14px}
.brand-name{font-family:"Montserrat",Arial,sans-serif;font-weight:700;font-size:15px;line-height:18px;color:var(--ink);letter-spacing:.5px}
.title{position:absolute;right:40px;top:46px;text-align:right}
.title-main{font-family:"Montserrat",Arial,sans-serif;font-weight:900;font-size:72px;line-height:66px;color:var(--blue);letter-spacing:-1px}
.title-sub{font-family:"Montserrat",Arial,sans-serif;font-weight:500;font-size:40px;line-height:44px;color:var(--ink);letter-spacing:17px;margin-right:-17px;margin-top:6px}

/* photo band */
.photo{position:absolute;left:0;top:166px;width:880px;height:307px;
  background:linear-gradient(120deg,#dfe8f1 0%,#eef2f6 35%,#c9d6e3 70%,#9fb2c6 100%)}

/* body */
.body{position:absolute;left:0;top:473px;width:880px;height:652px;background:var(--paper-soft)}
.intro{position:absolute;left:34px;top:16px;width:410px}
.company{font-family:"Montserrat",Arial,sans-serif;font-weight:800;font-size:34px;line-height:34px;color:var(--blue-head)}
.tagline{font-family:"Montserrat",Arial,sans-serif;font-weight:600;font-size:18px;line-height:21px;color:var(--ink);margin-top:8px;text-transform:uppercase}
.rule{width:44px;height:2px;background:var(--ink);margin:9px 0 14px}
.intro p{font-size:14px;line-height:18.5px;text-align:justify;margin-bottom:7px;color:var(--text)}

.goal{position:absolute;left:9px;top:359px;width:437px;height:136px;border-radius:8px;
  background:linear-gradient(90deg,#4f88c6,#6ea4d6);color:var(--white);padding:10px 24px}
.goal-title{font-family:"Montserrat",Arial,sans-serif;font-weight:900;font-size:64px;line-height:64px;letter-spacing:-1px}
.goal-text{font-size:21px;line-height:24px;font-weight:500;margin-top:8px}

.services{position:absolute;left:484px;top:9px;width:366px;height:488px;border-radius:10px;
  background:var(--blue-panel);color:var(--white);padding:6px 16px 0 18px}
.services-title{font-family:"Montserrat",Arial,sans-serif;font-weight:800;font-size:34px;line-height:42px;color:#d8e6f5;white-space:nowrap;letter-spacing:-.3px}
.group{display:flex;align-items:center;font-family:"Montserrat",Arial,sans-serif;font-weight:700;font-size:16px;line-height:20px;margin:3px 0 6px}
.group::after{content:"";flex:1;height:1px;background:rgba(255,255,255,.45);margin-left:8px}
.list{list-style:none;margin-bottom:6px}
.list li{position:relative;padding-left:22px;font-size:14.5px;line-height:19px;white-space:nowrap}
.list li::before{content:"";position:absolute;left:0;top:4.5px;width:11px;height:11px;border-radius:50%;background:#c9dcf1}
.list li::after{content:"";position:absolute;left:3.5px;top:7px;width:3px;height:5px;border:solid var(--blue-panel);border-width:0 1.6px 1.6px 0;transform:rotate(45deg)}

/* tools */
.tools{position:absolute;left:0;top:977px;width:880px;height:148px;background:var(--paper)}
.tool{position:absolute;display:flex;align-items:center;gap:8px;font-family:"Montserrat",Arial,sans-serif;font-weight:700;font-size:21px;white-space:nowrap}
.tool .dot{width:18px;height:18px;border-radius:50%;flex:none}
.tool .sq{width:18px;height:18px;flex:none}
.t1{left:48px;top:28px;color:#d3312b}
.t2{left:258px;top:28px;color:#2f8f3e}
.t3{left:455px;top:28px;color:#333}
.t4{left:692px;top:28px;color:#c3202e}
.t5{left:275px;top:96px;color:#1d6e86}
.t6{left:470px;top:96px;color:#2a6ab4}
.t7{left:590px;top:96px;color:#e8742c}

/* footer */
.footer{position:absolute;left:0;top:1125px;width:880px;height:75px;background:var(--blue-band);color:var(--white);text-align:center}
.contact-name{font-family:"Montserrat",Arial,sans-serif;font-weight:800;font-size:24px;margin-top:8px;line-height:28px}
.contact-role{font-family:"Raleway",Arial,sans-serif;font-weight:500;font-size:14px}
.contact-lines{display:flex;justify-content:center;gap:22px;margin-top:6px;font-family:"Raleway",Arial,sans-serif;font-weight:600;font-size:15.5px}
.contact-lines span{display:flex;align-items:center;gap:8px}
.contact-lines svg{width:15px;height:15px}
</style>
</head>
<body>
<div class="flyer">
  <div class="top-strip"></div>

  <header>
    <div class="brand">
      <div class="brand-mark"></div>
      <div class="brand-name">CORVANE PROJECT SERVICES</div>
    </div>
    <div class="title">
      <div class="title-main">CAPABILITY</div>
      <div class="title-sub">STATEMENT</div>
    </div>
  </header>

  <div class="photo" role="img" aria-label="Photo of colleagues' hands reviewing printed charts and documents at a desk"></div>

  <main class="body">
    <section class="intro">
      <h1 class="company">CORVANE PROJECT SERVICES LTD.</h1>
      <h2 class="tagline">is a leading project control consultancy based in Co Cork Ireland</h2>
      <div class="rule"></div>
      <p>For over 20 years we havebeen helping our clients to deliver complex projects and programs throughout mainland Europe.</p>
      <p>We are passionate about empower organisations to achieve their objectives, on time and on budget.</p>
      <p>We are continually innovating, evolving and learning, utilize the latest industry tools and techniques to deliver real value to our clients.</p>
    </section>

    <section class="goal">
      <div class="goal-title">OURGOAL</div>
      <div class="goal-text">is to make successful project delivery more achievable and repeatable.</div>
    </section>

    <section class="services">
      <h2 class="services-title">CORE SERVICES</h2>
      <h3 class="group">Planning and Scheduling</h3>
      <ul class="list">
        <li>Tender Planning</li>
        <li>Interactive Planning / Pull Planning</li>
        <li>EPCMV Planning &amp; Scheduling</li>
        <li>Schedule Earned Value Management</li>
        <li>Independent Schedule Quality Assessment</li>
        <li>Schedule Risk Analysis (Monte Carlo)</li>
        <li>Training</li>
      </ul>
      <h3 class="group">Management of Risk</h3>
      <ul class="list">
        <li>Risk Management Policies &amp; Procedures</li>
        <li>Risk Management Strategy</li>
        <li>Risk Registers</li>
        <li>Risk Improvement Planning</li>
        <li>Risk Response and Communication</li>
        <li>Risk Management Training</li>
      </ul>
      <h3 class="group">Cost Control</h3>
      <ul class="list">
        <li>Estimating &amp; Forecasting</li>
        <li>Earned Value Analysis</li>
        <li>Progress Reporting</li>
        <li>Cost Risk Analysis</li>
      </ul>
    </section>
  </main>

  <section class="tools" aria-label="Tools we use">
    <div class="tool t1"><span class="dot" style="background:#d3312b"></span>Tessera Planner</div>
    <div class="tool t2"><span class="sq" style="background:#2f8f3e"></span>Linea Project</div>
    <div class="tool t3"><span class="sq" style="background:#d9262c"></span>Orbis Schedule</div>
    <div class="tool t4">Waypoint Pro</div>
    <div class="tool t5"><span class="dot" style="background:#1d6e86"></span>RiskFrame</div>
    <div class="tool t6">Quorra</div>
    <div class="tool t7">| Metric</div>
  </section>

  <footer class="footer">
    <div class="contact-name">DEREK ASHFORD <span class="contact-role">(MANAGING DIRECTOR)</span></div>
    <div class="contact-lines">
      <span><svg viewBox="0 0 16 16"><circle cx="8" cy="8" r="8" fill="#fff"/><rect x="4" y="5" width="8" height="6" fill="none" stroke="#4c86c6" stroke-width="1.2"/><path d="M4 5l4 3 4-3" fill="none" stroke="#4c86c6" stroke-width="1.2"/></svg>INFO@CORVANESERVICES.IE</span>
      <span><svg viewBox="0 0 16 16"><circle cx="8" cy="8" r="8" fill="#fff"/><circle cx="8" cy="8" r="4.5" fill="none" stroke="#4c86c6" stroke-width="1.2"/><path d="M3.5 8h9M8 3.5v9" stroke="#4c86c6" stroke-width="1"/></svg>WWW.CORVANESERVICES.IE</span>
      <span><svg viewBox="0 0 16 16"><circle cx="8" cy="8" r="8" fill="#fff"/><path d="M5.5 4.5l1.5 0 .8 2-1 1c.5 1 1.2 1.7 2.2 2.2l1-1 2 .8v1.5c-3.5.5-7-3-6.5-6.5z" fill="#4c86c6"/></svg>+353 (0)870 555 014</span>
    </div>
  </footer>
</div>
</body>
</html>
```